BSC Flyer to attract applicants 11x17

Brightline Stagecraft Company provides crew for local concerts, filming, theater, and corporate events.
The flyer will be posted on bulletin boards at colleges with theater programs.
Our primary venues are historic theaters in downtown LA
Need a 11x17 poster to attract potential applicants/crew
I have attached a poster that one of our staff made that has all if the relevant info - but i know the poster can look much better than that. I have also attached many images and our logo. It is not necessary to use all of the images, or any of them. The two images of the theater interiors are the venues we operate so they would be the first to include. I can send additional info or images upon request. Thank you

Entertainment

• APPLY@BSCCREWHUB.LA

```html
<!DOCTYPE html>
<html lang="en">
<head>
<meta charset="utf-8">
<title>Brightline Stagecraft Company – Open Positions</title>
<link rel="stylesheet" href="https://fonts.googleapis.com/css2?family=Bebas+Neue&family=Poppins:wght@400;500;600;700&display=swap">
<style>
  :root {
    --stage-bg: #e4e7ef;
    --paper: #eeeeec;
    --paper-shade: #e2e2df;
    --brand-blue: #2250b8;
    --deep-navy: #1b2a5a;
    --ink: #161616;
    --rule: #9aa6c8;
    --white: #ffffff;
  }
  html, body {
    margin: 0;
    padding: 0;
    width: 1200px;
    height: 1200px;
    overflow: hidden;
    background: var(--stage-bg);
  }
  .canvas {
    width: 1200px;
    height: 1200px;
    display: flex;
    align-items: center;
    justify-content: center;
  }
  .flyer {
    width: 741px;
    height: 1144px;
    display: block;
    box-shadow: 0 6px 24px rgba(30, 40, 80, 0.18);
  }
  .paper { fill: var(--paper); }
  .paper-facet { fill: var(--paper-shade); opacity: 0.55; }
  .accent { fill: var(--brand-blue); }
  .accent-deep { fill: var(--deep-navy); }
  .brand-mark { fill: var(--brand-blue); }
  .brand-name {
    font-family: "Poppins", sans-serif;
    font-weight: 600;
    fill: var(--brand-blue);
  }
  .brand-name-main { font-size: 23px; letter-spacing: 0.2px; }
  .brand-name-sub { font-size: 13px; letter-spacing: 9px; }
  .tag-text {
    font-family: "Poppins", sans-serif;
    font-weight: 600;
    font-size: 27px;
    letter-spacing: 0.6px;
    fill: var(--white);
  }
  .headline {
    font-family: "Bebas Neue", sans-serif;
    font-size: 124px;
  }
  .headline .word-open { fill: var(--ink); }
  .headline .word-positions { fill: var(--brand-blue); }
  .lede {
    font-family: "Poppins", sans-serif;
    font-weight: 400;
    font-size: 20px;
    fill: var(--ink);
  }
  .divider { stroke: var(--rule); stroke-width: 1.2; }
  .cta-label {
    font-family: "Poppins", sans-serif;
    font-weight: 600;
    font-size: 22px;
    letter-spacing: 14px;
    fill: var(--ink);
  }
  .email-text {
    font-family: "Poppins", sans-serif;
    font-weight: 500;
    font-size: 19px;
    fill: var(--white);
  }
</style>
</head>
<body>
<main class="canvas">
  <svg class="flyer" viewBox="0 0 872 1345" xmlns="http://www.w3.org/2000/svg">
    <defs>
      <linearGradient id="venue-left-tones" x1="0" y1="0" x2="0.55" y2="1">
        <stop offset="0" stop-color="#2a2a1e"/>
        <stop offset="0.08" stop-color="#6b4a22"/>
        <stop offset="0.22" stop-color="#c8822e"/>
        <stop offset="0.38" stop-color="#e0a640"/>
        <stop offset="0.52" stop-color="#b8622a"/>
        <stop offset="0.66" stop-color="#d9a24a"/>
        <stop offset="0.8" stop-color="#a9742e"/>
        <stop offset="1" stop-color="#3a2a26"/>
      </linearGradient>
      <linearGradient id="venue-right-tones" x1="0" y1="0" x2="0" y2="1">
        <stop offset="0" stop-color="#e6a8c8"/>
        <stop offset="0.09" stop-color="#c8407a"/>
        <stop offset="0.16" stop-color="#5a2a6a"/>
        <stop offset="0.26" stop-color="#b86a6a"/>
        <stop offset="0.4" stop-color="#e0c08a"/>
        <stop offset="0.55" stop-color="#c89068"/>
        <stop offset="0.66" stop-color="#a0306a"/>
        <stop offset="0.76" stop-color="#5a3aa0"/>
        <stop offset="0.88" stop-color="#3a1a4a"/>
        <stop offset="1" stop-color="#2a1020"/>
      </linearGradient>
    </defs>

    <rect class="paper" x="0" y="0" width="872" height="1345"/>
    <polygon class="paper-facet" points="0,20 330,8 180,230 0,180"/>
    <polygon class="paper-facet" points="872,1000 872,1300 640,1320 760,1120"/>

    <!-- top edge band -->
    <polygon class="accent" points="0,0 697,0 0,20"/>

    <!-- venue photographs -->
    <polygon role="img" aria-label="Photo of an ornate gilded historic theater interior with balcony boxes and stage drapes"
             fill="url(#venue-left-tones)" points="0,249 515,249 0,1040"/>
    <polygon role="img" aria-label="Photo of a historic downtown theater auditorium with carved proscenium, stage and rows of red seats"
             fill="url(#venue-right-tones)" points="832,0 872,0 872,932 127,932"/>

    <!-- diagonal brand band -->
    <polygon class="accent" points="697,0 832,0 780,70 0,1092"/>
    <polygon class="accent-deep" points="0,1040 180,765 127,932 0,1092"/>

    <!-- brand name -->
    <circle class="brand-mark" cx="262" cy="106" r="46"/>
    <text class="brand-name brand-name-main" x="262" y="192" text-anchor="middle">BRIGHTLINE STAGECRAFT</text>
    <text class="brand-name brand-name-sub" x="266" y="214" text-anchor="middle">COMPANY</text>

    <!-- tag banner -->
    <polygon class="accent" points="197,979 682,979 662,1025 177,1025"/>
    <text class="tag-text" x="430" y="1012" text-anchor="middle">BRIGHTLINE STAGECRAFT HAS</text>

    <!-- headline -->
    <text class="headline" x="436" y="1131" text-anchor="middle"><tspan class="word-open">OPEN </tspan><tspan class="word-positions">POSITIONS</tspan></text>

    <text class="lede" x="436" y="1160" text-anchor="middle">We are looking for talented technicians to add to our roster of</text>
    <text class="lede" x="436" y="1186" text-anchor="middle">skilled professionals</text>

    <line class="divider" x1="85" y1="1210" x2="782" y2="1210"/>

    <text class="cta-label" x="443" y="1257" text-anchor="middle">SEND RESUME TO</text>

    <!-- email banner -->
    <polygon class="accent" points="285,1277 607,1277 587,1322 265,1322"/>
    <text class="email-text" x="436" y="1307" text-anchor="middle">APPLY@BSCCREWHUB.LA</text>

    <!-- bottom edge band -->
    <polygon class="accent" points="470,1345 872,1323 872,1345"/>
  </svg>
</main>
</body>
</html>
```